Lotus Leaf Kitchen Road Billboard

Road Billboard I need all of this information on it
Authentic Thai Food Bangkok Style
6.5 Miles on the right
4126 Maple Ridge Rd Otto NC
828-555-4172

```html
<!DOCTYPE html>
<html lang="en">
<head>
<meta charset="utf-8">
<title>Lotus Leaf Kitchen – Road Billboard</title>
<link rel="stylesheet" href="https://fonts.googleapis.com/css2?family=Fraunces:ital,opsz,wght@1,144,900&family=Montserrat:wght@700&family=Roboto+Condensed:wght@700&display=swap">
<style>
  :root {
    --orange: #fb8a2e;
    --green: #008f35;
    --white: #ffffff;
    --ink: #0a0a0a;
    --gold: #e8c224;
    --night: #121517;
    --ember: #f47a1c;
  }
  * { margin: 0; padding: 0; box-sizing: border-box; }
  html, body { width: 1200px; height: 670px; overflow: hidden; background: var(--white); }
  .billboard { position: relative; width: 1200px; height: 670px; overflow: hidden; }
  .billboard-art { position: absolute; inset: 0; }
  .headline {
    position: absolute; left: 80px; top: 30px;
    font-family: "Fraunces", Georgia, serif; font-style: italic; font-weight: 900;
    font-size: 88px; line-height: 83px; color: var(--ink); letter-spacing: -1px;
  }
  .distance {
    position: absolute; left: 134px; top: 412px; color: var(--white);
    font-family: "Montserrat", Arial, sans-serif; font-weight: 700;
  }
  .distance-number { font-size: 62px; line-height: 66px; letter-spacing: -1px; }
  .distance-unit { font-size: 38px; margin-left: 4px; }
  .distance-note { display: block; font-size: 37px; line-height: 40px; margin-top: -2px; }
  .contact {
    position: absolute; left: 86px; top: 540px;
    font-family: "Roboto Condensed", Arial, sans-serif; font-weight: 700;
    font-size: 38px; line-height: 50px; color: var(--ink);
  }
  .brand-name {
    position: absolute; left: 952px; top: 604px;
    font-family: "Fraunces", Georgia, serif; font-style: italic; font-weight: 900;
    font-size: 24px; color: var(--gold);
  }
</style>
</head>
<body>
<div class="billboard">
  <svg class="billboard-art" width="1200" height="670" viewBox="0 0 1200 670" xmlns="http://www.w3.org/2000/svg">
    <defs>
      <radialGradient id="flame-glow" cx="0.3" cy="0.55" r="0.75">
        <stop offset="0" stop-color="#ffd27a"/>
        <stop offset="0.3" stop-color="#f7901f"/>
        <stop offset="0.65" stop-color="#7a2a08"/>
        <stop offset="1" stop-color="#121517"/>
      </radialGradient>
    </defs>
    <rect class="food-photo" x="560" y="0" width="640" height="670" fill="url(#flame-glow)"
          role="img" aria-label="Photo of shrimp, broccoli and vegetables tossed above a flaming wok"/>
    <path class="panel" d="M0 0 H587 C620 60 632 150 627 210 C622 300 592 360 597 410 C602 450 614 480 613 520 C611 600 606 640 609 670 H0 Z"
          fill="var(--orange)" stroke="var(--white)" stroke-width="26" paint-order="stroke"/>
    <path class="direction-band" d="M0 410 H554 L607 465 L554 521 H0 Z" fill="var(--green)"/>
    <g class="direction-arrow" fill="var(--white)">
      <rect x="0" y="450" width="126" height="23"/>
      <rect x="370" y="452" width="180" height="20"/>
      <path d="M505 420 L584 462 L522 510 L514 500 L560 466 L498 432 Z"/>
    </g>
  </svg>

  <h1 class="headline">Authentic<br>Thai Food<br>Bangkok<br>Stylet</h1>

  <p class="distance">
    <span class="distance-number">6.5</span><span class="distance-unit">Miles</span>
    <span class="distance-note">on the right</span>
  </p>

  <p class="contact">4126 Maple Ridge Rd Otto NC<br>828-555-4172</p>

  <p class="brand-name">Lotus Leaf Kitchen</p>
</div>
</body>
</html>
```